Velvet Dune is a premium Spa and Salon only professional tanning brand.

We need a email template/newsletter that we can send to our client base any time we would like to share information with them.
Whether this is launching our Christmas gift, or sharing up and coming training dates it will be another avenue for us to stay in touch with our clients.
We like to think ourselves as the 'Marchetti handbag' in the tanning world, Velvet Dune is a brand that is desirable and exclusive and has people hooked once they trial the brand and are blown away by the results.
www.velvet-dune.com

```html
<!DOCTYPE html>
<html lang="en">
<head>
<meta charset="utf-8">
<title>Velvet Dune Newsletter</title>
<link href="https://fonts.googleapis.com/css2?family=Quicksand:wght@400;500;700&display=swap" rel="stylesheet">
<style>
  :root {
    --page-bg: #f3ece6;
    --sheet-bg: #f9f5f1;
    --panel-bg: #fdfbf9;
    --wine: #7a2a22;
    --rust: #843426;
    --copper: #b06e48;
    --tan: #b98a63;
    --body-text: #9a4a3a;
    --ink: #2e2e2e;
    --footer-text: #f0ddd3;
  }
  * { margin: 0; padding: 0; box-sizing: border-box; }
  html, body { width: 1200px; height: 1000px; overflow: hidden; }
  body {
    background: var(--page-bg);
    font-family: "Quicksand", sans-serif;
    position: relative;
  }
  .newsletter {
    position: absolute; left: 248px; top: 60px;
    width: 704px; height: 880px;
    background: var(--sheet-bg);
    box-shadow: 0 4px 18px rgba(0,0,0,0.18);
  }
  .brand-name {
    position: absolute; left: 88px; top: 50px;
    width: 226px;
    font-weight: 700; font-size: 46px; line-height: 42px;
    color: var(--wine); text-transform: uppercase; letter-spacing: 1px;
  }
  .brand-name span { display: block; }
  .brand-name .brand-second { text-align: right; }
  .header-rule {
    position: absolute; left: 360px; top: 57px;
    width: 2px; height: 79px; background: var(--rust);
  }
  .issue-date {
    position: absolute; left: 367px; top: 54px;
    font-size: 13px; font-weight: 500; color: var(--copper);
    text-transform: uppercase; letter-spacing: 0.1px;
  }
  .hero {
    position: absolute; left: 88px; top: 177px;
    width: 528px; height: 254px;
    background:
      radial-gradient(ellipse 34% 60% at 20% 40%, rgba(40,40,40,0.55) 0%, rgba(70,70,70,0.25) 55%, rgba(0,0,0,0) 100%),
      radial-gradient(ellipse 22% 45% at 30% 78%, rgba(120,120,120,0.45) 0%, rgba(0,0,0,0) 100%),
      radial-gradient(ellipse 30% 40% at 75% 35%, rgba(255,255,255,0.55) 0%, rgba(255,255,255,0) 100%),
      linear-gradient(100deg, #4f4f4f 0%, #8d8d8d 22%, #cfcfcf 45%, #e2e2e2 70%, #e9e9e9 100%);
  }
  .hero-link {
    position: absolute; right: 12px; bottom: 10px;
    font-weight: 700; font-size: 25px; color: var(--ink);
    text-transform: uppercase; letter-spacing: 0.3px;
    text-shadow: 0 1px 2px rgba(255,255,255,0.6);
  }
  .letter {
    position: absolute; left: 88px; top: 439px;
    width: 329px; height: 326px;
    background: var(--panel-bg);
    padding: 29px 10px 0 19px;
    color: var(--body-text);
  }
  .letter-greeting { font-weight: 700; font-size: 14.5px; color: var(--wine); margin-bottom: 20px; }
  .letter p { font-size: 15px; line-height: 18px; text-align: justify; margin-bottom: 18px; }
  .letter strong { color: var(--wine); font-weight: 700; }
  .letter-site {
    position: absolute; left: 0; right: 0; bottom: 26px;
    text-align: center; font-size: 15px; color: var(--tan);
  }
  .product {
    position: absolute; left: 427px; top: 439px;
    width: 189px; height: 326px;
    background:
      radial-gradient(ellipse 22% 22% at 30% 60%, rgba(150,75,45,0.35) 0%, rgba(150,75,45,0) 100%),
      radial-gradient(ellipse 20% 20% at 60% 58%, rgba(150,75,45,0.28) 0%, rgba(150,75,45,0) 100%),
      linear-gradient(90deg, #f4f1ee 0%, #e6e3e0 4%, #ffffff 14%, #f7f5f3 36%, #e9e6e3 40%, #ffffff 48%, #f8f6f4 68%, #ebe8e5 72%, #ffffff 80%, #ffffff 100%);
  }
  .organic-badge { position: absolute; right: 0; top: 6px; }
  .product-link {
    position: absolute; left: 0; right: 0; top: 251px; height: 40px;
    background: var(--copper); color: #fff;
    font-weight: 700; font-size: 23px; line-height: 40px;
    padding-left: 10px; text-transform: uppercase;
  }
  .footer {
    position: absolute; left: 0; bottom: 0;
    width: 704px; height: 88px; background: var(--rust);
    color: var(--footer-text); font-size: 10.5px;
  }
  .footer-links { position: absolute; left: 88px; top: 22px; list-style: none; line-height: 17px; }
  .footer-email { position: absolute; left: 237px; top: 21px; }
  .social-dot {
    position: absolute; left: 468px; top: 29px;
    width: 32px; height: 32px; border-radius: 50%;
    background: var(--copper);
  }
  .footer-brand {
    position: absolute; left: 530px; top: 29px; width: 86px;
    font-weight: 700; font-size: 17px; line-height: 16px;
    color: var(--copper); text-transform: uppercase;
  }
  .footer-brand span { display: block; }
  .footer-brand .brand-second { text-align: right; }
</style>
</head>
<body>
  <main class="newsletter">
    <header>
      <div class="brand-name"><span>Velvet</span><span class="brand-second">Dune</span></div>
      <div class="header-rule"></div>
      <div class="issue-date">Newsletter, Thursday, 12 October</div>
    </header>

    <section class="hero" role="img" aria-label="Black and white photo of a woman's bare back with falling autumn leaves">
      <span class="hero-link">Wonderful News ›</span>
    </section>

    <article class="letter">
      <div class="letter-greeting">Ladies and Gentleman,</div>
      <p>We’ve got lots of exciting news for you today. First off, we’ve launched a new <strong>site</strong>, released our Orbit phone app Velvet Dune™ in the Orbit Market.</p>
      <p>Thanks!</p>
      <p>Velvet Dune</p>
      <div class="letter-site">www.velvet-dune.com</div>
    </article>

    <section class="product" role="img" aria-label="Two white tanning spray bottles with copper leaf print">
      <svg class="organic-badge" width="84" height="84" viewBox="0 0 84 84" aria-hidden="true">
        <circle cx="42" cy="42" r="40" fill="var(--copper)"/>
      </svg>
      <span class="product-link">Revolution ›</span>
    </section>

    <footer class="footer">
      <ul class="footer-links">
        <li>Unsubscribe</li>
        <li>Manage Subscription</li>
        <li>Forward to Friend</li>
      </ul>
      <div class="footer-email">hello@velvet-dune.com</div>
      <div class="social-dot" aria-label="Social page"></div>
      <div class="footer-brand"><span>Velvet</span><span class="brand-second">Dune</span></div>
    </footer>
  </main>
</body>
</html>
```